Finch Haulage Ltd

We need an A5 size (UK size) flyer to advertise our new business which is called Finch Haulage.
Domestic and Commercial Waste Clearance Services.
Please have the question in bold "Do you have a pile of junk you need to dispose of?"
We collect all kinds of junk or rubbish from homes and businesses across Kent, Sussex and South London.
No fuss, no mess!
A low cost, hassle free alternative to skip hire.
Licensed by the Landcare Board and fully insured (this can be in small print at the bottom).
Please put the Recycle symbol somewhere.
Our tagline on our vehicle is "We Clear More, For Less!"
We'd like the flyer to be bold and eye-catching (to catch the eye of the homeowner or business owner while it's sitting on their doormat).
We need our telephone, website and email to be prominent. Maybe saying "Call today for a free quote"
Tel. 01734 586019
Email: info@finchhaulage.example.co.uk
www.finchhaulage.example.co.uk
Target Market(s)
Our market will be homes and small businesses around Kent, Sussex and South London.

```html
<!DOCTYPE html>
<html lang="en">
<head>
<meta charset="UTF-8">
<title>Finch Haulage – Waste Clearance Flyer</title>
<link rel="stylesheet" href="https://fonts.googleapis.com/css2?family=Abril+Fatface&family=PT+Serif&family=PT+Sans:wght@400;700&family=Open+Sans:wght@400;600;700&display=swap">
<style>
  :root {
    --backdrop: #b9b9c0;
    --paper: #ffffff;
    --grey-text: #5e5e5e;
    --ink: #1d1d1d;
    --green-dark: #1e6b2a;
    --brand-green: #3a9a3a;
  }
  * { box-sizing: border-box; margin: 0; padding: 0; }
  html, body {
    width: 1200px; height: 900px; overflow: hidden;
    background: var(--backdrop);
  }
  .flyer {
    position: absolute; left: 303px; top: 30px;
    width: 594px; height: 840px;
    background: var(--paper);
    overflow: hidden;
    box-shadow: 0 6px 24px rgba(0,0,0,0.25);
  }
  .flyer__wave { position: absolute; inset: 0; width: 100%; height: 100%; }
  .brand {
    position: absolute; top: 44px; right: 70px;
    display: flex; align-items: center; gap: 10px;
    font-family: "Open Sans", sans-serif; font-weight: 700;
    font-size: 28px; color: var(--brand-green);
  }
  .brand__mark { width: 18px; height: 18px; border-radius: 50%; background: var(--brand-green); }
  .tagline {
    position: absolute; top: 128px; left: 44px;
    font-family: "Open Sans", sans-serif; font-weight: 700;
    font-size: 17px; letter-spacing: 0.5px; color: var(--grey-text);
    white-space: nowrap;
  }
  .headline {
    position: absolute; top: 160px; left: 10px; right: 10px;
    text-align: center;
    font-family: "Abril Fatface", serif; font-weight: 400;
    font-size: 40px; line-height: 1.2; color: var(--grey-text);
    white-space: nowrap;
  }
  .headline span { display: block; }
  .intro {
    position: absolute; top: 330px; left: 20px; right: 20px;
    text-align: center;
    font-family: "PT Serif", serif;
    font-size: 20px; line-height: 1.3; color: var(--ink);
    white-space: nowrap;
  }
  .recycle-icon {
    position: absolute; top: 470px; left: 30px;
    width: 230px; height: 220px;
  }
  .slogan {
    position: absolute; top: 455px; left: 290px;
    font-family: "Abril Fatface", serif;
    font-size: 42px; line-height: 1.25; color: var(--green-dark);
    white-space: nowrap;
  }
  .slogan span { display: block; padding-left: 40px; }
  .contact {
    position: absolute; top: 600px; left: 250px; right: 10px;
    text-align: center; color: var(--ink); white-space: nowrap;
  }
  .contact__cta { font-family: "PT Sans", sans-serif; font-size: 23px; }
  .contact__tel { font-family: "Open Sans", sans-serif; font-size: 25px; margin-top: 6px; }
  .contact__line { font-family: "PT Serif", serif; font-size: 17px; line-height: 1.4; }
  .licence {
    position: absolute; bottom: 22px; left: 0; right: 0;
    text-align: center;
    font-family: "Open Sans", sans-serif; font-size: 11px; color: var(--ink);
  }
</style>
</head>
<body>
  <article class="flyer">
    <svg class="flyer__wave" viewBox="0 0 594 840" preserveAspectRatio="none" aria-hidden="true">
      <defs>
        <linearGradient id="waveFill" x1="0" y1="0" x2="0" y2="1">
          <stop offset="0" stop-color="#4f9e24"/>
          <stop offset="0.5" stop-color="#6db33a"/>
          <stop offset="1" stop-color="#8cc63f"/>
        </linearGradient>
      </defs>
      <path d="M0 490 C140 390 340 300 594 255 L594 840 L0 840 Z" fill="url(#waveFill)"/>
    </svg>

    <div class="brand"><span class="brand__mark"></span>Finch Haulage</div>
    <p class="tagline">We Clear More, For Less!</p>
    <h1 class="headline">
      <span>Do you have a pile of</span>
      <span>junk you need to dispose</span>
      <span>of ?</span>
    </h1>
    <p class="intro">We collect all kinds of junk or rubbish from<br>homes and businesses.<br>A low cost, hassle free alternative to<br>skip hire.</p>

    <svg class="recycle-icon" viewBox="0 0 200 190" role="img" aria-label="Recycle symbol">
      <g id="recycleArrow" fill="#1e6b2a" stroke="#1e6b2a">
        <path d="M38.4 144.4 L70.6 84.6" stroke-width="22" fill="none"/>
        <polygon points="90,95 51.2,74.2 89.5,49.4" stroke="none"/>
      </g>
      <use href="#recycleArrow" transform="rotate(120 100 116.7)"/>
      <use href="#recycleArrow" transform="rotate(240 100 116.7)"/>
    </svg>

    <p class="slogan">No fuss,<span>no mess!</span></p>

    <div class="contact">
      <p class="contact__cta">Call today for a free quote</p>
      <p class="contact__tel">Tel. 01734 586019</p>
      <p class="contact__line">Email: info@finchhaulage.example.co.uk</p>
      <p class="contact__line">www.finchhaulage.example.co.uk</p>
    </div>

    <p class="licence">Licensed by the Landcare Board and fully insured.</p>
  </article>
</body>
</html>
```